International professional tennis coach needs a book cover design

This is my 2nd published book, the first one was a #1 on the best seller. I'm looking for a world class book cover design for this new book. The name of my first book was 5 Baseline Habits to Unlock Your Rally Rhythm, located on Brimlow.com

The title of the new book:

Title: The Craft of Steady Rallies
Subtitle: Building a Tactical Margin by Way of Opponent Insight

I'm uploading our new CRAFT OF STEADY logo that I'd like for you to use as the centerpiece of the book design along with a 21st century design feel that incorporates what the book topic is below::

--> This book is about building competitive intelligence by using tennis data analytics to develop and expand a player's strategic advantage for match play. <--

The colors we would like to use are Blue, Yellow, and Green. These shades of these colors should be bold! (You will see the bold color examples of blues, yellows, and greens that I'm talking about in the logos that are attached here, especially the colors for my Tennis GridRally App logo.

I will upload the Tennis GridRally logo which should go somewhere on the back cover design (small size maybe in the bottom corner).

This book is revolutionary to the standard way of teaching tennis, it is based on a decade of recording and gathering tennis data analytics and then we created on-court practice games to develop better decision making in players for the competitive edge.

My websites are www.elevatedrillzone.com and www.craftofsteadyrallies.com

```html
<!DOCTYPE html>
<html lang="en">
<head>
<meta charset="UTF-8">
<title>The Craft of Steady Rallies — Book Cover</title>
<link href="https://fonts.googleapis.com/css2?family=Roboto+Condensed:wght@700&family=Roboto:wght@400;700;900&display=swap" rel="stylesheet">
<style>
  :root{
    --blue:#1368b8;
    --yellow:#f2b705;
    --green:#a6c813;
    --ink:#1c1c1c;
    --paper:#ffffff;
    --stage:#e9e9e6;
    --spine-shade:#f1f1f1;
    --photo-a:#6f8a5a;
    --photo-b:#3b4046;
  }
  *{box-sizing:border-box;margin:0;padding:0}
  html,body{width:1200px;height:800px;overflow:hidden;background:var(--stage)}
  body{font-family:"Roboto",sans-serif;color:var(--ink)}
  .cover-wrap{
    position:absolute;left:30px;top:20px;width:1140px;height:760px;
    display:flex;background:var(--paper);box-shadow:0 4px 18px rgba(0,0,0,.12)
  }
  /* ---------- back cover ---------- */
  .back-cover{width:530px;height:100%;padding:44px 44px 30px 46px;position:relative}
  .back-title{font-family:"Roboto Condensed",sans-serif;font-weight:700;font-size:27px;line-height:1;text-align:center;letter-spacing:.2px}
  .back-subtitle{font-size:12.5px;text-transform:uppercase;text-align:center;line-height:1.25;margin-top:6px}
  .blurb p{font-size:11.6px;line-height:1.38;margin-top:13px}
  .blurb p:first-child{margin-top:22px}
  .author-bio{display:flex;gap:14px;margin-top:20px;align-items:flex-start}
  .author-photo{flex:0 0 132px;height:170px;background:linear-gradient(160deg,var(--photo-a),var(--photo-b))}
  .author-bio p{font-size:11.6px;line-height:1.38;text-align:justify}
  .app-mark{position:absolute;left:46px;bottom:30px;display:flex;align-items:center;gap:6px;
    font-size:11px;font-weight:700;color:var(--blue)}
  .app-mark .dot{width:16px;height:16px;border-radius:50%;background:var(--blue)}
  /* ---------- spine ---------- */
  .spine{width:80px;height:100%;background:linear-gradient(90deg,var(--paper),var(--spine-shade) 55%,var(--paper));
    display:flex;flex-direction:column;justify-content:space-between;align-items:center;padding:30px 0 40px}
  .spine-title,.spine-author{writing-mode:vertical-rl;white-space:nowrap}
  .spine-title{font-family:"Roboto Condensed",sans-serif;font-weight:700;font-size:30px}
  .spine-author{font-weight:700;font-size:20px;letter-spacing:3px;text-transform:uppercase}
  /* ---------- front cover ---------- */
  .front-cover{width:530px;height:100%;padding:56px 46px 46px;display:flex;flex-direction:column;align-items:center;
    box-shadow:inset 8px 0 14px -10px rgba(0,0,0,.15)}
  .series-mark{display:flex;align-items:center;gap:10px;font-weight:900;font-size:28px;color:var(--blue);
    text-transform:uppercase;height:120px}
  .series-mark .dot{width:22px;height:22px;border-radius:50%;background:var(--blue)}
  .front-title{font-family:"Roboto Condensed",sans-serif;font-weight:700;text-align:center;line-height:.92;margin-top:18px}
  .front-title span{display:block}
  .t-line-1{font-size:96px;color:var(--blue)}
  .t-line-2{font-size:96px;color:var(--blue)}
  .t-line-3{font-size:124px;color:var(--yellow)}
  .t-line-4{font-size:124px;color:var(--green)}
  .front-subtitle{font-size:19px;text-transform:uppercase;text-align:center;line-height:1.2;margin-top:16px}
  .front-author{margin-top:auto;font-weight:900;font-size:30px;letter-spacing:5px;text-transform:uppercase}
  .blue{color:var(--blue)}.yellow{color:var(--yellow)}.green{color:var(--green)}
</style>
</head>
<body>
<main class="cover-wrap">
  <section class="back-cover">
    <h2 class="back-title"><span class="blue">THE CRAFT OF</span> <span class="yellow">STEADY</span> <span class="green">RALLIES</span></h2>
    <p class="back-subtitle">Building a Tactical Margin<br>by Way of Opponent Insight</p>
    <div class="blurb">
      <p>A practical guide on how to win more matches by becoming a more efficient and effective competitor.</p>
      <p>As a tennis player you have the ability to play better matches and win more of them. The Craft of Steady Rallies gives you a system to improve. We start with the individual game of the set itself. Our system examines your physical and mental progression, enabling you to upgrade your movement and performance from shot to shot and point to point. Our system seamlessly integrates the technical (physical) aspects with the tactical (mental/emotional) components, providing a comprehensive approach to elevate this performance.</p>
      <p>We aim to give you much more than how to hit great shots. Irrespective of your current skill level, we will provide you with a detailed strategic and tactical plan to enhance your performance, leading to improved results and increased success in your matches.</p>
      <p>The Craft of Steady Rallies emphasizes the importance of shifting focus from oneself to the opponent, encouraging players to analyze and understand their adversaries. By bringing the opponent back to the forefront of their thinking, the player creates the best possible context in which to improve as a competitor. In this book, we present a groundbreaking approach to tennis data analytics that seamlessly integrates match performance with practice sessions, and vice versa.</p>
    </div>
    <div class="author-bio">
      <div class="author-photo" role="img" aria-label="Portrait photo of the author on a tennis court"></div>
      <p>Dorran Vessick is regarded as one of the leading strategy and tactical coaches in the world today. He is the Creator of Tennis GridRally, the world's first Tennis Tracking App that maps and charts match play based on the rally length of a point. Dorran is a Best Selling Author of the book "5 Baseline Habits to Unlock Your Rally Rhythm" and the CoFounder of The Craft of Steady Rallies promoting coach, player, and parent development. He is often sought after by coaches around the world to design the practice court in a way that revolutionizes a player's mindset to successfully negotiate the pressures of competitive match play.</p>
    </div>
    <div class="app-mark"><span class="dot"></span>Tennis GridRally</div>
  </section>

  <section class="spine">
    <h2 class="spine-title"><span class="blue">THE CRAFT OF</span> <span class="yellow">STEADY</span> <span class="green">RALLIES</span></h2>
    <p class="spine-author">Dorran Vessick</p>
  </section>

  <section class="front-cover">
    <div class="series-mark"><span class="dot"></span>Craft of Steady</div>
    <h1 class="front-title">
      <span class="t-line-1">THE CRAFT</span>
      <span class="t-line-2">OF</span>
      <span class="t-line-3">STEADY</span>
      <span class="t-line-4">RALLIES</span>
    </h1>
    <p class="front-subtitle">Building a Tactical Margin<br>by Way of Opponent Insight</p>
    <p class="front-author">Dorran Vessick</p>
  </section>
</main>
</body>
</html>
```